Business Card for New Business

Please design a business card using our logo and font files. This is only one card for one person, as listed in details section.

Industry/Entity Type

Business

Contact Information for Business Card

Carl Voserby

Phone 240.318.6624
Cell 703.581.4096
Email carl@moltravex.com

www.moltravex.com

Address
18250 Brennick Lane #314
Damascus, MD 20715

Font styles to use
Sans Serif

Requirements
Must have
• Information listed in detail section. Must be standard card size.

```html
<!DOCTYPE html>
<html lang="en">
<head>
<meta charset="utf-8">
<title>Moltravex Productions – Business Card</title>
<link rel="stylesheet" href="https://fonts.googleapis.com/css2?family=Roboto:wght@400;700&display=swap">
<style>
  :root {
    --bg: #e6e6e4;
    --card-dark: #1f1f1f;
    --card-light: #ffffff;
    --accent: #d9531e;
    --accent-deep: #c4461a;
    --ink: #4a4a4a;
    --ink-soft: #6b6b6b;
    --rule: #c9c9c9;
  }
  * { margin: 0; padding: 0; box-sizing: border-box; }
  html, body { width: 1200px; height: 900px; overflow: hidden; }
  body {
    background: var(--bg);
    font-family: "Roboto", Arial, sans-serif;
    position: relative;
  }
  .card {
    position: absolute;
    left: 337px;
    width: 525px;
    height: 300px;
    box-shadow: 0 6px 18px rgba(0,0,0,0.18);
    overflow: hidden;
  }
  .card-back { top: 100px; background: var(--card-dark); }
  .card-front { top: 470px; background: var(--card-light); }

  .brand {
    display: flex;
    align-items: center;
    gap: 10px;
  }
  .brand-mark {
    width: 14px; height: 14px;
    border-radius: 50%;
    background: var(--accent);
    flex: none;
  }
  .brand-name {
    font-family: "Roboto", Arial, sans-serif;
    font-weight: 400;
    color: var(--accent);
    line-height: 1.15;
  }
  .card-back .brand {
    position: absolute;
    left: 0; right: 0; top: 130px;
    justify-content: center;
  }
  .card-back .brand-name { font-size: 34px; }
  .card-back .brand-mark { width: 20px; height: 20px; }

  .card-front .brand {
    position: absolute;
    left: 30px; top: 92px;
    width: 240px;
  }
  .card-front .brand-name { font-size: 22px; }

  .divider {
    position: absolute;
    left: 286px; top: 66px;
    width: 1px; height: 120px;
    background: var(--rule);
  }
  .contact {
    position: absolute;
    left: 302px; top: 62px;
    color: var(--ink);
    font-size: 12px;
    line-height: 1.35;
  }
  .contact .person {
    color: var(--accent);
    font-weight: 700;
    font-size: 16px;
    line-height: 1.1;
  }
  .contact .role { color: var(--ink-soft); font-size: 11.5px; margin-bottom: 10px; }
  .contact .address { margin-bottom: 6px; }
  .contact-list { list-style: none; }
  .contact-list li { display: flex; align-items: center; gap: 6px; height: 17px; }
  .contact-list svg { width: 10px; height: 10px; fill: var(--accent); flex: none; }

  .accent-band {
    position: absolute;
    left: 0; bottom: 0;
    width: 100%; height: 62px;
    background: linear-gradient(90deg, var(--accent) 0%, var(--accent-deep) 100%);
  }
</style>
</head>
<body>

<section class="card card-back">
  <div class="brand">
    <span class="brand-mark"></span>
    <p class="brand-name">Moltravex Productions</p>
  </div>
</section>

<section class="card card-front">
  <div class="accent-band" role="img" aria-label="Decorative orange and black swoosh along the bottom of the card"></div>

  <div class="brand">
    <span class="brand-mark"></span>
    <p class="brand-name">Moltravex Productions</p>
  </div>

  <div class="divider"></div>

  <div class="contact">
    <p class="person">Carl Voserby</p>
    <p class="role">President</p>
    <p class="address">18250 Brennick Lane #314<br>Damascus, MD 20715</p>
    <ul class="contact-list">
      <li><svg viewBox="0 0 10 10"><path d="M2,0.5 L3.6,2.6 L2.6,3.6 C3.2,5 4.8,6.6 6.4,7.4 L7.4,6.4 L9.5,8 L8.4,9.5 C4.4,9 1,5.6 0.5,1.6 Z"/></svg>240.318.6624</li>
      <li><svg viewBox="0 0 10 10"><path d="M2.5,0 H7.5 V10 H2.5 Z M3.3,1 V8 H6.7 V1 Z"/></svg>703.581.4096</li>
      <li><svg viewBox="0 0 10 10"><path d="M0,1.5 H10 V8.5 H0 Z M0.8,2.2 L5,5.5 L9.2,2.2 Z"/></svg>carl@moltravex.com</li>
      <li><svg viewBox="0 0 10 10"><path d="M5,0 A5,5 0 1 0 5,10 A5,5 0 1 0 5,0 Z M5,1 C4,2.5 4,7.5 5,9 C6,7.5 6,2.5 5,1 Z M1,4.5 H9 V5.5 H1 Z" fill-rule="evenodd"/></svg>www.moltravex.com</li>
    </ul>
  </div>
</section>

</body>
</html>
```